Brine - Pop/Rock Album Artwork

Brine are a London based Rock/Indie band and this is our 2nd album. We require CD cover artwork.
Here is the artwork for our first album: https://www.vendrilo.co.uk/gp/product/X913QK44Z2?ie=UTF8&*Version*=1&*entries*=0
We like the following attached CD Covers and we are in the same genre music as these bands.
The Album will be called "Paper Hollow", the band name "BRINE" should be uppercase. Ideally the name "BRINE" will be designed in such a way that we can use this font on badges and as a Logo itself.
The track listing is:-
1 Unspun
2. 40 Tides
3. Rusty Gale
4. Kestrels
5. Bellows
6. Fold the Amber
7. Herons
8. Palmora
9. Out by Dusk
10. Pale Ember
11. Unfurl
This project should really just cover the front page of the artwork for a digital CD artwork to be used on Cadenzo and Wavvel.
Please do listen to our music here: https://echovault.com/brine

```html
<!DOCTYPE html>
<html lang="en">
<head>
<meta charset="utf-8">
<title>BRINE – From Paper Hollow</title>
<link rel="stylesheet" href="https://fonts.googleapis.com/css2?family=Montserrat:wght@400;700&display=swap">
<style>
  :root {
    --ink: #000000;
    --paper: #ffffff;
    --gold: #cdb36c;
    --mane-light: #d9a85a;
    --mane-mid: #b98334;
    --mane-dark: #6e4818;
  }
  * { margin: 0; padding: 0; box-sizing: border-box; }
  html, body { width: 1200px; height: 1200px; overflow: hidden; background: var(--ink); }
  .cover {
    position: relative;
    width: 1200px;
    height: 1200px;
    background: var(--ink);
    font-family: "Montserrat", sans-serif;
    overflow: hidden;
  }
  .cover-photo {
    position: absolute;
    left: 0;
    top: 0;
    width: 860px;
    height: 1200px;
    background:
      radial-gradient(ellipse 62% 55% at 38% 48%, var(--mane-light) 0%, var(--mane-mid) 45%, rgba(110,72,24,0.85) 72%, rgba(0,0,0,0) 100%),
      linear-gradient(90deg, var(--mane-mid) 0%, var(--mane-dark) 55%, rgba(0,0,0,0) 100%);
  }
  .band-name {
    position: absolute;
    right: 40px;
    top: 22px;
    font-weight: 700;
    font-size: 192px;
    line-height: 1;
    letter-spacing: 2px;
    color: var(--paper);
  }
  .album-title {
    position: absolute;
    right: 40px;
    top: 228px;
    font-weight: 700;
    font-size: 24px;
    letter-spacing: 15px;
    margin-right: -15px;
    color: var(--paper);
    white-space: nowrap;
  }
  .track-list {
    position: absolute;
    right: 40px;
    top: 548px;
    list-style: none;
    text-align: right;
    font-weight: 400;
    font-size: 43px;
    line-height: 56.8px;
    color: var(--gold);
  }
</style>
</head>
<body>
  <main class="cover">
    <div class="cover-photo" role="img" aria-label="Photograph of a roaring lion in profile, golden mane against a black background"></div>
    <h1 class="band-name">BRINE</h1>
    <p class="album-title">From Paper Hollow</p>
    <ol class="track-list">
      <li>1. Unspun</li>
      <li>2. 40 Tides</li>
      <li>3. Rusty Gale</li>
      <li>4. Kestrels</li>
      <li>5. Bellows</li>
      <li>6. Fold the Amber</li>
      <li>7. Herons</li>
      <li>8. Palmora</li>
      <li>9. Out by Dusk</li>
      <li>10. Pale Ember</li>
      <li>11. Unfurl</li>
    </ol>
  </main>
</body>
</html>
```